Webdesign für  Photovoltaikanlagen und E-Ladeinfrastruktur
Webdesign für Photovoltaikanlagen und E-Ladeinfrastruktur
Zielgruppe
Die LURAN Energy GmbH ist ein Spezialist für die Planung und Projektierung von Photovoltaikanlagen und E-Ladeinfrastruktur.
Aufgabenstellung
- Design-Tool: Adobe Photoshop
- Hinweis: Die Firma wird sich neue aufstellen, was das Leistungsangebot betrifft. Sie können sich deshalb nur bedingt an der derzeitigen Website orientieren, alle fremden Logos (wie z.b. VOSKA) dürfen nicht mehr genutzt werden
- Gern hätten wir einen 'frischen' Slogan im headerbild

```html
<!DOCTYPE html>
<html lang="de">
<head>
<meta charset="utf-8">
<title>LURAN Energy GmbH – Energie- und Ladelösungen</title>
<link rel="stylesheet" href="https://fonts.googleapis.com/css2?family=Inter:wght@400;500;600&display=swap">
<style>
:root{
  --green:#16705c;
  --link:#1aa083;
  --sand:#e8c38f;
  --ink:#1f2a2a;
  --text:#2c3434;
  --blue-bg:#eaf2f9;
  --mint-bg:#d5f0eb;
  --footer-bg:#dadddc;
  --rule:#e6eef4;
}
*{margin:0;padding:0;box-sizing:border-box}
html,body{width:1200px;height:3098px;overflow:hidden}
body{position:relative;font-family:"Inter",sans-serif;color:var(--text);background:#fff}
a{color:inherit;text-decoration:none}

.hero{position:absolute;left:0;top:0;width:1200px;height:697px;overflow:hidden}
.hero-photo{position:absolute;inset:0;background:linear-gradient(180deg,#0d3a4a 0%,#2174c0 16%,#3a8fd8 45%,#86c0ec 70%,#6f8fb4 88%,#34465e 100%)}
.logo-word{position:absolute;font-weight:600;color:#fff;letter-spacing:1px}
.hero .logo-word{left:66px;top:40px;font-size:30px}
.nav{position:absolute;top:50px;left:426px;display:flex;gap:31px;font-size:14px;font-weight:600;color:#fff}
.btn{position:absolute;display:flex;align-items:center;justify-content:center;background:var(--sand);color:var(--ink);font-size:14px;font-weight:600;border-radius:3px}
.btn-top{left:921px;top:35px;width:212px;height:48px}
.hero-title{position:absolute;left:117px;top:196px;width:540px;font-size:41px;line-height:44px;font-weight:500;color:var(--ink);letter-spacing:-.3px}
.hero-text{position:absolute;left:117px;top:337px;width:510px;font-size:13.2px;line-height:22.6px;color:#1d2a33}
.btn-hero{left:117px;top:452px;width:212px;height:48px}

.section{position:absolute;left:0;width:1200px}
.about{top:697px;height:469px;background:#fff}
.about-rule{position:absolute;left:1082px;top:0;width:6px;height:469px;background:var(--rule)}
.h2{font-size:31px;font-weight:500;color:var(--green);letter-spacing:.3px}
.centered{position:absolute;text-align:center}
.about .h2{left:0;width:1200px;top:136px}
.body-text{font-size:13.3px;line-height:22.5px}
.about .body-text{left:255px;width:690px;top:177px}
.more{font-size:13.5px;font-weight:500;color:var(--link);text-decoration:underline;text-underline-offset:3px}
.about .more{left:0;width:1200px;top:332px}

.charging{top:1166px;height:620px;background:var(--blue-bg)}
.solar{top:1786px;height:616px;background:var(--mint-bg)}
.card{position:absolute;width:535px;height:397px;background:#fff;border-radius:22px 0 22px 0;padding:36px 42px}
.card .h2{margin-bottom:6px}
.card .body-text{margin-bottom:20px}
.charging .card{left:107px;top:111px}
.solar .card{left:600px;top:109px}
.photo-frame{position:absolute;background:var(--green)}
.photo{position:absolute}
.charging .photo-frame{left:791px;top:238px;width:261px;height:293px}
.charging .photo{left:724px;top:95px;width:321px;height:427px;background:linear-gradient(160deg,#123a9a 0%,#1f52d6 55%,#4a6fc8 100%)}
.solar .photo-frame{left:225px;top:234px;width:261px;height:291px}
.solar .photo{left:159px;top:90px;width:320px;height:427px;background:linear-gradient(180deg,#7493dc 0%,#8aa6e4 35%,#3a5ab8 65%,#4f7a6a 88%,#6f9e2a 100%)}

.planning{top:2402px;height:436px;background:#fff}
.planning-rule{position:absolute;left:134px;top:0;width:4px;height:436px;background:var(--mint-bg)}
.planning .h2{left:0;width:1200px;top:96px}
.planning .body-text{left:208px;width:784px;top:138px}
.planning .more{left:0;width:1200px;top:312px}

.footer{top:2838px;height:260px;background:var(--footer-bg);font-size:13.4px;color:var(--text)}
.footer-links{position:absolute;left:137px;top:95px;display:flex;gap:18px}
.footer-tagline{position:absolute;left:137px;top:137px;line-height:21.5px}
.footer .logo-word{left:0;width:1200px;text-align:center;top:86px;font-size:24px;color:var(--green)}
.copyright{left:0;width:1200px;top:137px}
.address{position:absolute;right:132px;top:91px;text-align:right;line-height:23.5px;font-style:normal}
.address strong{font-weight:600}
</style>
</head>
<body>

<header class="hero">
  <div class="hero-photo" role="img" aria-label="Photovoltaik-Freiflächenanlage unter blauem Himmel mit Schleierwolken"></div>
  <a class="logo-word" href="#">LURAN</a>
  <nav class="nav"><a href="#">Home</a><a href="#">Unternehmen</a><a href="#">Leistungen</a><a href="#">Kontakt</a></nav>
  <a class="btn btn-top" href="#">Jetzt Angebot anfordern</a>
  <h1 class="hero-title">Revolutionäre Energie- und Ladelösungen für eine nachhaltige Zukunft</h1>
  <p class="hero-text">Willkommen bei LURAN. Wir bieten maßgeschneiderte Lösungen für die Planung und Projektierung von Photovoltaikanlagen und E-Ladeinfrastruktur. Revolutionieren Sie Ihre Energieversorgung mit unseren innovativen und nachhaltigen Lösungen. Kontaktieren Sie uns noch heute, um mehr zu erfahren</p>
  <a class="btn btn-hero" href="#">Jetzt Angebot anfordern</a>
</header>

<section class="section about">
  <div class="about-rule"></div>
  <h2 class="h2 centered">WIR SIND LURAN</h2>
  <p class="body-text centered">Wir sind ein führendes Unternehmen in der Planung und Projektierung von Photovoltaikanlagen und E-Ladeinfrastruktur und haben uns zum Ziel gesetzt, eine nachhaltige Zukunft zu schaffen. Unser erfahrenes Team von Ingenieuren und Planern arbeitet eng mit unseren Kunden zusammen, um individuelle Lösungen zu entwickeln, die auf deren Bedürfnisse zugeschnitten sind. Bei LURAN sind wir davon überzeugt, dass die Zukunft der Energieversorgung sauber und nachhaltig sein muss. Erfahren Sie mehr über uns und unsere Vision auf unserer Unternehmen-Seite.</p>
  <a class="more centered" href="#">Mehr erfahren</a>
</section>

<section class="section charging">
  <div class="card">
    <h2 class="h2">E-LADEINFRASTRUKTUR</h2>
    <p class="body-text">Bei LURAN sind wir stolz darauf, unseren Kunden innovative und maßgeschneiderte Lösungen für E-Ladeinfrastruktur zu bieten. Mit der steigenden Nachfrage nach Elektrofahrzeugen wird es immer wichtiger, zuverlässige und effiziente Ladelösungen anzubieten. Unsere erfahrenen Ingenieure und Planer arbeiten eng mit unseren Kunden zusammen, um individuelle Lösungen für die E-Ladeinfrastruktur zu entwickeln, die perfekt auf ihre Bedürfnisse abgestimmt sind. Von der Planung und Projektierung bis zur Installation und Wartung bieten wir unseren Kunden eine komplette Palette von Dienstleistungen an. Erfahren Sie mehr darüber, wie wir die E-Ladeinfrastruktur revolutionieren können.</p>
    <a class="more" href="#">Mehr erfahren</a>
  </div>
  <div class="photo-frame"></div>
  <div class="photo" role="img" aria-label="Blaues Elektroauto beim Laden mit orangefarbenem Ladekabel"></div>
</section>

<section class="section solar">
  <div class="photo-frame"></div>
  <div class="photo" role="img" aria-label="Reihen von Solarmodulen auf grüner Wiese unter blauem Himmel"></div>
  <div class="card">
    <h2 class="h2">PHOTOVOLTAIK PROFIS</h2>
    <p class="body-text">Als Experten für Photovoltaikanlagen sind wir bei LURAN bestrebt, nachhaltige Energieversorgung für unsere Kunden zu schaffen. Photovoltaik ist eine bewährte und zukunftsfähige Technologie, die es ermöglicht, Sonnenenergie in Strom umzuwandeln. Unsere erfahrenen Ingenieure und Planer arbeiten eng mit unseren Kunden zusammen, um individuelle Photovoltaik-Lösungen zu entwickeln, die perfekt auf ihre Bedürfnisse abgestimmt sind. Wir bieten eine komplette Palette von Dienstleistungen an, von der Planung und Projektierung bis zur Installation und Wartung. Erfahren Sie mehr darüber, wie wir Ihnen helfen können, saubere und nachhaltige Energie zu erzeugen.</p>
    <a class="more" href="#">Mehr erfahren</a>
  </div>
</section>

<section class="section planning">
  <div class="planning-rule"></div>
  <h2 class="h2 centered">PLANUNG UND PROJEKTIERUNG</h2>
  <p class="body-text centered">Bei LURAN bieten wir eine umfassende Planung und Projektierung von Photovoltaikanlagen und E-Ladeinfrastruktur an. Unser erfahrenes Team von Ingenieuren und Planern arbeitet eng mit unseren Kunden zusammen, um individuelle Lösungen zu entwickeln, die auf deren Bedürfnisse zugeschnitten sind. Wir bieten eine detaillierte Planung und Projektierung von Anfang bis Ende an, um sicherzustellen, dass die Anlage oder die Ladeinfrastruktur effektiv und effizient funktioniert. Unsere umfassenden Kenntnisse und unsere Erfahrung ermöglichen es uns, maßgeschneiderte Lösungen zu entwickeln, die auf Ihre spezifischen Anforderungen zugeschnitten sind. Erfahren Sie mehr darüber, wie wir Ihnen helfen können, Ihre nachhaltigen Energieprojekte zu realisieren</p>
  <a class="more centered" href="#">Mehr erfahren</a>
</section>

<footer class="section footer">
  <nav class="footer-links"><a href="#">Kontakt</a><a href="#">Datenschutz</a><a href="#">Impressum</a></nav>
  <p class="footer-tagline">Revolutionäre Energie-<br>und Ladelösungen für<br>eine nachhaltige Zukunft</p>
  <span class="logo-word">LURAN</span>
  <p class="centered copyright">© 2023 LURAN Energy GmbH</p>
  <address class="address"><strong>LURAN Energy GmbH</strong><br>Lindenhofweg 14<br>04105 Musterstadt<br>Tel.: 0341 555 018-20<br>Fax: 0341 555 018-211</address>
</footer>

</body>
</html>
```